Criação de Papelaria (6 itens) para Arquitetura
" Sou recém formada em Design de Interiores e pretendo começar a divulgar meu negócio. Já fiz alguns trabalhos / projetos, mas ainda não consegui alavancar minha marca. Meu foco será a realização de projetos residenciais, comerciais e empresariais. As atividades vão desde a entrevista inicial para entendimento das necessidades do cliente, passando pela preparação dos projetos com imagens renderizadas, plantas baixas, projetos de marcenaria, iluminação, gesso etc., incluindo também acompanhamento a lojas para escolha de materiais / móveis até o acompanhamento da obra e fiscalização dos trabalhos executados por terceiros. "

```html
<!DOCTYPE html>
<html lang="pt-BR">
<head>
<meta charset="utf-8">
<title>Lara Meireles – Envelope</title>
<link rel="stylesheet" href="https://fonts.googleapis.com/css2?family=Raleway:wght@300;400&display=swap">
<style>
  :root {
    --backdrop: #d9d8dc;
    --paper-light: #57536a;
    --paper-dark: #403c4d;
    --rose-light: #f6cdbd;
    --rose: #e3a18c;
    --rose-deep: #c98571;
    --ink-soft: #e9e4ea;
  }
  * { margin: 0; padding: 0; box-sizing: border-box; }
  html, body { width: 1200px; height: 1200px; overflow: hidden; }
  body {
    background: var(--backdrop);
    font-family: "Raleway", sans-serif;
    position: relative;
  }
  .envelope {
    position: absolute;
    top: 216px;
    width: 528px;
    height: 768px;
    background: radial-gradient(ellipse at 50% 40%, var(--paper-light), var(--paper-dark) 85%);
    box-shadow: 0 6px 18px rgba(0, 0, 0, 0.25);
    overflow: hidden;
  }
  .envelope--back { left: 60px; }
  .envelope--front { left: 612px; }

  .flap {
    position: absolute;
    top: 0; left: 0; right: 0;
    height: 96px;
    background: linear-gradient(100deg, var(--rose-deep), var(--rose-light) 45%, var(--rose) 100%);
    border-radius: 0 0 22px 22px;
    display: flex;
    align-items: center;
    justify-content: center;
  }
  .flap__name {
    font-weight: 400;
    font-size: 15px;
    letter-spacing: 4px;
    color: #a86a58;
  }

  .contact {
    position: absolute;
    left: 26px;
    top: 598px;
    list-style: none;
    font-size: 9px;
    color: var(--ink-soft);
    line-height: 1.35;
  }
  .contact__item {
    display: flex;
    align-items: center;
    gap: 8px;
    margin-bottom: 10px;
  }
  .contact__icon { width: 14px; height: 14px; flex: none; }

  .signature {
    position: absolute;
    font-weight: 300;
    color: var(--ink-soft);
    white-space: nowrap;
    transform: translateX(-50%);
  }
  .signature--back {
    left: 420px;
    top: 664px;
    font-size: 22px;
    letter-spacing: 2px;
  }
  .signature--front {
    left: 50%;
    top: 398px;
    font-size: 34px;
    letter-spacing: 3px;
  }

  .rule {
    position: absolute;
    left: 0; right: 0;
    height: 4px;
    background: linear-gradient(90deg, var(--rose-deep), var(--rose-light) 50%, var(--rose));
  }
  .rule--back { top: 744px; }
  .rule--back-thin { top: 738px; height: 1px; opacity: 0.7; }
  .rule--front { top: 724px; }
  .rule--front-thin { top: 718px; height: 1px; opacity: 0.7; }
</style>
</head>
<body>
  <section class="envelope envelope--back" aria-label="Verso do envelope">
    <div class="flap"><span class="flap__name">LARA MEIRELES</span></div>

    <ul class="contact">
      <li class="contact__item">
        <svg class="contact__icon" viewBox="0 0 14 14" aria-hidden="true">
          <circle cx="7" cy="7" r="7" fill="#e3a18c"/>
          <path d="M4.6 3.8c.4-.3.8-.2 1 .2l.6 1.2c.1.3 0 .6-.2.8l-.4.3c.4.9 1.1 1.6 2 2l.3-.4c.2-.2.5-.3.8-.2l1.2.6c.4.2.5.6.2 1-.6.8-1.6.9-2.5.4A7 7 0 0 1 4.2 6.3c-.5-.9-.4-1.9.4-2.5z" fill="#403c4d"/>
        </svg>
        <span>+55 11 4000-1020<br>+55 11 98000-3040</span>
      </li>
      <li class="contact__item">
        <svg class="contact__icon" viewBox="0 0 14 14" aria-hidden="true">
          <circle cx="7" cy="7" r="7" fill="#e3a18c"/>
          <circle cx="7" cy="7" r="3.6" fill="none" stroke="#403c4d" stroke-width="0.9"/>
          <path d="M3.4 7h7.2M7 3.4c-1.4 1.9-1.4 5.3 0 7.2M7 3.4c1.4 1.9 1.4 5.3 0 7.2" fill="none" stroke="#403c4d" stroke-width="0.8"/>
        </svg>
        <span>www.laramei.com.br</span>
      </li>
      <li class="contact__item">
        <svg class="contact__icon" viewBox="0 0 14 14" aria-hidden="true">
          <circle cx="7" cy="7" r="7" fill="#e3a18c"/>
          <path d="M7 3a2.6 2.6 0 0 1 2.6 2.6C9.6 7.6 7 11 7 11S4.4 7.6 4.4 5.6A2.6 2.6 0 0 1 7 3z" fill="#403c4d"/>
          <circle cx="7" cy="5.6" r="0.9" fill="#e3a18c"/>
        </svg>
        <span>Rua das Acácias, 120 - Centro<br>01000-000 São Paulo</span>
      </li>
    </ul>

    <p class="signature signature--back">LARA MEIRELES</p>
    <div class="rule rule--back-thin"></div>
    <div class="rule rule--back"></div>
  </section>

  <section class="envelope envelope--front" aria-label="Frente do envelope">
    <p class="signature signature--front">LARA MEIRELES</p>
    <div class="rule rule--front-thin"></div>
    <div class="rule rule--front"></div>
  </section>
</body>
</html>
```